Redesign current business card for food company

i would like to redesign my business card. our company is food company, our product range from chips, juices, milk and etc (mostly dried food stuff).
I want o keep same logo but , the rest is open to new design.
you can check at our website about our company www.velqorafare.com

Target Market(s)

most of food company

Industry/Entity Type

Business

Contact Information for Business Card

I want to keep more to blue color...

Colors
3176b5
abd036

Requirements
Must have
• our old logo
Nice to have
• we do not mind to have nice material on bus card in order to accomplish nice design. for example: using spot uv, embossed and etc.

```html
<!DOCTYPE html>
<html lang="en">
<head>
<meta charset="utf-8">
<title>Velqora Business Card</title>
<link href="https://fonts.googleapis.com/css2?family=Montserrat:wght@400;500;600&display=swap" rel="stylesheet">
<style>
  :root {
    --page-bg: #e9e7ef;
    --card-blue: #3f36a8;
    --card-blue-light: #6c68c9;
    --card-blue-deep: #2b2290;
    --accent-cyan: #2fb6d6;
    --brand-blue: #3176b5;
    --brand-green: #abd036;
    --paper: #ffffff;
    --text-light: #ffffff;
  }
  html, body {
    margin: 0;
    padding: 0;
    width: 1200px;
    height: 913px;
    overflow: hidden;
    background: var(--page-bg);
    font-family: "Montserrat", sans-serif;
  }
  .sheet {
    width: 1200px;
    height: 913px;
    display: flex;
    align-items: center;
    justify-content: center;
    gap: 40px;
  }
  .card {
    position: relative;
    width: 540px;
    height: 309px;
    border-radius: 16px;
    overflow: hidden;
    box-shadow: 0 10px 28px rgba(30, 20, 80, 0.25);
  }
  .card-front {
    background: linear-gradient(160deg, var(--card-blue-light) 0%, var(--card-blue) 45%, var(--card-blue-deep) 100%);
  }
  .front-art {
    position: absolute;
    inset: 0;
    width: 100%;
    height: 100%;
  }
  .brand-mark {
    position: absolute;
    left: 50px;
    top: 128px;
    display: flex;
    align-items: center;
    gap: 10px;
  }
  .brand-dot {
    width: 14px;
    height: 14px;
    border-radius: 50%;
    background: var(--brand-green);
  }
  .brand-name {
    font-size: 44px;
    font-weight: 600;
    color: var(--brand-blue);
    letter-spacing: -0.5px;
  }
  .contact-block {
    position: absolute;
    right: 28px;
    top: 30px;
    text-align: right;
    color: var(--text-light);
  }
  .person-name {
    font-size: 17px;
    font-weight: 600;
    color: var(--accent-cyan);
    margin: 0;
  }
  .person-role {
    font-size: 11px;
    color: var(--accent-cyan);
    margin: 2px 0 14px;
  }
  .address-line {
    font-size: 11.5px;
    line-height: 1.35;
    margin: 0;
  }
  .contact-list {
    list-style: none;
    margin: 14px 0 0;
    padding: 0;
  }
  .contact-list li {
    font-size: 11.5px;
    line-height: 1.45;
    display: flex;
    justify-content: flex-end;
    align-items: center;
    gap: 7px;
  }
  .contact-icon {
    width: 10px;
    height: 10px;
    flex: none;
  }
  .card-back {
    background: linear-gradient(160deg, var(--card-blue-light) 0%, var(--card-blue) 40%, var(--card-blue-deep) 100%);
  }
  .back-mark {
    position: absolute;
    left: 0;
    right: 0;
    top: 92px;
    text-align: center;
    font-size: 84px;
    font-weight: 600;
    color: rgba(120, 115, 205, 0.55);
    letter-spacing: -1px;
  }
  .back-url {
    position: absolute;
    left: 0;
    right: 0;
    bottom: 62px;
    text-align: center;
    font-size: 15px;
    color: var(--text-light);
    letter-spacing: 0.3px;
  }
</style>
</head>
<body>
<main class="sheet">
  <section class="card card-front" aria-label="Card front">
    <svg class="front-art" viewBox="0 0 540 309" preserveAspectRatio="none" aria-hidden="true">
      <path d="M0 0 H150 Q330 40 320 309 H0 Z" fill="var(--paper)"/>
      <path d="M150 0 Q330 40 320 309" fill="none" stroke="var(--accent-cyan)" stroke-width="3"/>
      <path d="M162 0 Q342 40 332 309" fill="none" stroke="var(--paper)" stroke-width="2.5"/>
      <path d="M174 0 Q354 40 344 309" fill="none" stroke="var(--paper)" stroke-width="2"/>
      <path d="M186 0 Q366 40 356 309" fill="none" stroke="var(--card-blue-light)" stroke-width="2"/>
    </svg>

    <div class="brand-mark">
      <span class="brand-dot"></span>
      <span class="brand-name">Velqora</span>
    </div>

    <div class="contact-block">
      <p class="person-name">Marcus Delavenne</p>
      <p class="person-role">President</p>
      <p class="address-line">Velqora Enterprises Corp.</p>
      <p class="address-line">2418 W Alder St.</p>
      <p class="address-line">Ridgefield CA 90412</p>
      <ul class="contact-list">
        <li>555 240 1188
          <svg class="contact-icon" viewBox="0 0 10 10"><path d="M2 1 L4 1 L4.6 3 L3.5 3.8 Q4.5 5.8 6.2 6.5 L7 5.4 L9 6 L9 8 Q5 9 2.5 6 Q1 4 2 1 Z" fill="var(--accent-cyan)"/></svg>
        </li>
        <li>555 240 1177
          <svg class="contact-icon" viewBox="0 0 10 10"><rect x="1" y="3" width="8" height="5" rx="1" fill="var(--accent-cyan)"/><rect x="3" y="1" width="4" height="2.5" fill="var(--accent-cyan)"/></svg>
        </li>
        <li>555 318 4267
          <svg class="contact-icon" viewBox="0 0 10 10"><rect x="2.5" y="0.5" width="5" height="9" rx="1" fill="none" stroke="var(--accent-cyan)" stroke-width="1.2"/></svg>
        </li>
        <li>marcus@velqorafare.com
          <svg class="contact-icon" viewBox="0 0 10 10"><rect x="0.8" y="2" width="8.4" height="6" rx="1" fill="none" stroke="var(--accent-cyan)" stroke-width="1.1"/><path d="M1 2.5 L5 5.5 L9 2.5" fill="none" stroke="var(--accent-cyan)" stroke-width="1.1"/></svg>
        </li>
        <li>www.velqorafare.com
          <svg class="contact-icon" viewBox="0 0 10 10"><circle cx="5" cy="5" r="4" fill="none" stroke="var(--accent-cyan)" stroke-width="1.1"/><path d="M1 5 H9 M5 1 Q2.5 5 5 9 Q7.5 5 5 1" fill="none" stroke="var(--accent-cyan)" stroke-width="0.9"/></svg>
        </li>
      </ul>
    </div>
  </section>

  <section class="card card-back" aria-label="Card back">
    <div class="back-mark">Velqora</div>
    <div class="back-url">www.velqorafare.com</div>
  </section>
</main>
</body>
</html>
```